Business Card Design

We need a new business card design for a company based in Southlake, TX. We provide business consulting services in the information technology / services space. We like variations of the color blue, aqua, black, light tan, and white. Would like "cool" tones. The design should clearly communicate professionalism. Think outside the box - we don't want something "typical". Our company name is "Vantrell Advisory, LLC".
Updates

Thank you all for your submissions. We have seen some very creative and inspired designs. We have made a decision and will be moving forward with that design. Appreciate all of the hard work.

Industry/Entity Type

Information Technology

Contact Information for Business Card

Denise Harlow Trumbey
482 West Maple Ridge Dr.
Southlake, TX 76185

```html
<!DOCTYPE html>
<html lang="en">
<head>
<meta charset="utf-8">
<title>Vantrell Advisory, LLC – Business Card</title>
<link rel="stylesheet" href="https://fonts.googleapis.com/css2?family=Arimo:wght@400;500;700&display=swap">
<style>
  :root {
    --backdrop: #e6eaea;
    --card: #ffffff;
    --ink: #111111;
    --aqua: #74fbcb;
    --name-aqua: #6ef0c6;
  }
  html, body {
    margin: 0;
    padding: 0;
    width: 1200px;
    height: 1200px;
    overflow: hidden;
    background: var(--backdrop);
    font-family: "Arimo", Arial, sans-serif;
  }
  .canvas {
    position: relative;
    width: 1200px;
    height: 1200px;
  }
  .business-card {
    position: absolute;
    left: 100px;
    top: 314px;
    width: 1000px;
    height: 572px;
    background: var(--card);
    box-shadow: 0 10px 30px rgba(0, 0, 0, 0.08);
    color: var(--ink);
    text-align: center;
  }
  .company-name {
    position: absolute;
    top: 64px;
    left: 0;
    right: 0;
    margin: 0;
    font-size: 42px;
    font-weight: 700;
    letter-spacing: 0.2px;
  }
  .person {
    position: absolute;
    top: 152px;
    left: 0;
    right: 0;
  }
  .person-name {
    margin: 0;
    font-size: 35px;
    font-weight: 400;
    color: var(--name-aqua);
    line-height: 1.1;
  }
  .person-title {
    margin: 2px 0 0;
    font-size: 18px;
    font-weight: 400;
  }
  .contact-list {
    position: absolute;
    top: 318px;
    left: 0;
    right: 0;
    margin: 0;
    padding: 0;
    list-style: none;
    font-size: 25px;
    line-height: 1.2;
  }
  .address-band {
    position: absolute;
    left: 0;
    right: 0;
    bottom: 0;
    height: 98px;
    background: var(--aqua);
    display: flex;
    align-items: center;
    justify-content: center;
  }
  .address {
    margin: 0;
    font-style: normal;
    font-size: 25px;
    font-weight: 500;
  }
</style>
</head>
<body>
<main class="canvas">
  <section class="business-card">
    <h1 class="company-name">Vantrell Advisory, LLC</h1>
    <div class="person">
      <p class="person-name">Denise Harlow</p>
      <p class="person-title">C.E.O</p>
    </div>
    <ul class="contact-list">
      <li class="contact-phone">+00 555 0142876</li>
      <li class="contact-email">deniseharlow@vantrelladvisory.com</li>
      <li class="contact-web">www.vantrelladvisory.com</li>
    </ul>
    <div class="address-band">
      <address class="address">Trumbey 482 West Maple Ridge Dr. Southlake, TX 76185</address>
    </div>
  </section>
</main>
</body>
</html>
```